Business Card Design Project

www.tallorivault.com is our website. We are a technology company that provides brokers, lawyers and accountants with an cloud based paperless facilitation and revenue stream that facilitates their clients Health spending accounts.

Target Market(s)

Insurance brokers, lawyers and accountants

Industry/Entity Type

Business

```html
<!DOCTYPE html>
<html lang="en">
<head>
<meta charset="utf-8">
<title>Tallori Business Card</title>
<link rel="stylesheet" href="https://fonts.googleapis.com/css2?family=PT+Sans:wght@700&family=PT+Sans+Narrow:wght@400&display=swap">
<style>
  :root {
    --page: #ffffff;
    --card: #ffffff;
    --card-edge: #2b2b2b;
    --sky: #29a9e0;
    --deep-blue: #1575bd;
    --ink: #333333;
    --accent: #fbb040;
    --band-text: #ffffff;
  }
  * { margin: 0; padding: 0; box-sizing: border-box; }
  html, body {
    width: 1200px;
    height: 896px;
    overflow: hidden;
    background: var(--page);
  }
  .card {
    position: absolute;
    left: 197px;
    top: 195px;
    width: 818px;
    height: 529px;
    background: var(--card);
    border: 1px solid var(--card-edge);
    overflow: hidden;
  }
  .brand {
    position: absolute;
    left: 40px;
    top: 142px;
    display: flex;
    align-items: center;
    gap: 14px;
  }
  .brand-dot {
    width: 34px;
    height: 34px;
    border-radius: 50%;
    background: var(--sky);
  }
  .brand-name {
    font-family: "PT Sans", sans-serif;
    font-weight: 700;
    font-size: 62px;
    line-height: 1;
    color: var(--sky);
  }
  .contact {
    position: absolute;
    right: 51px;
    top: 172px;
    text-align: right;
  }
  .contact-name {
    font-family: "PT Sans", sans-serif;
    font-weight: 700;
    font-size: 42px;
    line-height: 50px;
    color: var(--deep-blue);
  }
  .contact-line {
    font-family: "PT Sans Narrow", sans-serif;
    font-size: 26px;
    line-height: 37px;
  }
  .contact-line.address { color: var(--sky); }
  .contact-line.email { color: var(--ink); }
  .accent-bar {
    position: absolute;
    right: 0;
    top: 173px;
    width: 29px;
    height: 195px;
    background: var(--accent);
  }
  .web-band {
    position: absolute;
    left: 0;
    bottom: 0;
    width: 100%;
    height: 62px;
    background: var(--deep-blue);
    display: flex;
    align-items: center;
    justify-content: center;
  }
  .web-address {
    font-family: "PT Sans Narrow", sans-serif;
    font-size: 28px;
    color: var(--band-text);
  }
</style>
</head>
<body>
  <div class="card">
    <div class="brand">
      <span class="brand-dot"></span>
      <span class="brand-name">tallori</span>
    </div>

    <div class="contact">
      <p class="contact-name">Mara Linden</p>
      <p class="contact-line address">Suite 240, 4120 - 9th Street NE</p>
      <p class="contact-line address">Riverton, AB&nbsp; T4K 2M9</p>
      <p class="contact-line email">sales@tallorivault.com</p>
      <p class="contact-line email">admin@tallorivault.com</p>
    </div>

    <div class="accent-bar"></div>

    <div class="web-band">
      <span class="web-address">www.tallorivault.com</span>
    </div>
  </div>
</body>
</html>
```